Vesk Architecture

We are a architectural design and build company working between scales 1/1000 to 1/1 we want people to understand our difference from our design experience and quality.we build hotels restourants and office spaces.Our company name is Vesk architecture to mind sustainability.

We want to write our adress phone and work spesifications on the card and we want our logo as backround.

Ps:you could find the logo adress and phone box numbers from the web:www.veskmimarlik-ornek.com

Target Market(s)

Who looks for experts.

Industry/Entity Type

Architecture

Requirements
Must have
• Design is over everything.
Should not have
• we don want it to be colorfull

```html
<!DOCTYPE html>
<html lang="tr">
<head>
<meta charset="utf-8">
<title>Vesk Mimarlık – Kartvizit</title>
<link href="https://fonts.googleapis.com/css2?family=Barlow:wght@300;400&display=swap" rel="stylesheet">
<style>
  :root {
    --page-bg: #ffffff;
    --card-bg: #ffffff;
    --card-edge: #555555;
    --ink: #9c9c9c;
    --ink-soft: #a8a8a8;
  }
  * { margin: 0; padding: 0; box-sizing: border-box; }
  html, body {
    width: 1200px;
    height: 834px;
    overflow: hidden;
    background: var(--page-bg);
    font-family: "Barlow", Arial, sans-serif;
  }
  .business-card {
    position: absolute;
    left: 54px;
    top: 54px;
    width: 940px;
    height: 570px;
    background: var(--card-bg);
    border: 1.5px solid var(--card-edge);
    color: var(--ink);
  }
  .brand {
    position: absolute;
    left: 76px;
    top: 150px;
    font-weight: 300;
    color: var(--ink);
  }
  .brand-name {
    display: block;
    font-size: 150px;
    line-height: 1;
    letter-spacing: 6px;
  }
  .brand-sub {
    display: block;
    margin-top: 12px;
    font-size: 36px;
    letter-spacing: 5px;
  }
  .person {
    position: absolute;
    left: 572px;
    top: 246px;
    width: 270px;
    text-align: center;
    font-weight: 300;
  }
  .person-name {
    font-size: 31px;
    letter-spacing: 1.5px;
    line-height: 1.2;
  }
  .person-role {
    font-size: 24px;
    letter-spacing: 1px;
    margin-top: 2px;
  }
  .contact {
    position: absolute;
    left: 70px;
    top: 464px;
    font-size: 23px;
    font-weight: 400;
    letter-spacing: 0.6px;
    color: var(--ink-soft);
    line-height: 42px;
    white-space: nowrap;
  }
  .sep { margin: 0 10px; }
</style>
</head>
<body>
  <article class="business-card">
    <div class="brand">
      <span class="brand-name">vesk</span>
      <span class="brand-sub">MİMARLIK</span>
    </div>

    <div class="person">
      <p class="person-name">deniz arman kaya</p>
      <p class="person-role">mimar</p>
    </div>

    <address class="contact">
      <p>yelken mah. liman cad. ada sok.<span class="sep">|</span>no : 7 beşiktaş<span class="sep">|</span>istanbul</p>
      <p>t. 0212 555 04 17<span class="sep">|</span>f. 0212 555 04 18<span class="sep">|</span>e.veskmimarlik@ornek.com</p>
    </address>
  </article>
</body>
</html>
```